Electronic hardware design and manufacturer needing a new business card design.

We need a new business card design consisting of a double sided design adhering to brand and logo guidelines attached. I also want to incorporate something that recognizes our 25th year in business ("EST 2001" or something like that....).

Need extra days to review

Need extra days to review

```html
<!DOCTYPE html>
<html lang="en">
<head>
<meta charset="utf-8">
<title>Northwind Telemetry Corp. – Business Card</title>
<link rel="stylesheet" href="https://fonts.googleapis.com/css2?family=Arimo:wght@400;700&display=swap">
<style>
  :root {
    --page: #e9e6e1;
    --card-light: #ffffff;
    --card-dark: #0c2434;
    --brand-navy: #12283a;
    --brand-gold: #f2a516;
    --brand-orange: #e8741c;
    --text-light: #d6dde3;
  }
  * { box-sizing: border-box; margin: 0; padding: 0; }
  html, body {
    width: 1200px; height: 900px; overflow: hidden;
    background: var(--page);
    font-family: "Arimo", Arial, sans-serif;
  }
  .sheet {
    width: 1200px; height: 900px;
    display: flex; flex-direction: column;
    align-items: center; justify-content: center; gap: 40px;
  }
  .card {
    width: 700px; height: 400px;
    border-radius: 28px;
    position: relative;
    overflow: hidden;
    box-shadow: 0 10px 30px rgba(0,0,0,0.18);
  }
  .card--front {
    background: var(--card-light);
    display: flex; flex-direction: column;
    align-items: center; justify-content: center; gap: 10px;
  }
  .card--back {
    background: var(--card-dark);
    color: var(--text-light);
  }
  .lockup {
    display: flex; flex-direction: column; align-items: center; gap: 6px;
  }
  .wordmark {
    display: flex; align-items: center; gap: 14px;
    font-weight: 700;
    font-size: 44px;
    letter-spacing: 0.5px;
    line-height: 1.1;
  }
  .wordmark__square {
    width: 22px; height: 22px;
    background: var(--brand-gold);
  }
  .card--front .wordmark { color: var(--brand-navy); }
  .card--back .wordmark { color: var(--text-light); }
  .established {
    font-size: 13px;
    font-weight: 700;
    letter-spacing: 3px;
    color: var(--brand-orange);
  }
  .card--back .established { color: var(--brand-gold); }
  .web-address {
    color: var(--brand-orange);
    font-size: 17px;
    letter-spacing: 0.5px;
  }
  .back-logo {
    position: absolute; top: 50px; left: 0; right: 0;
    display: flex; justify-content: center;
  }
  .contact {
    position: absolute; top: 165px; left: 40px; right: 40px;
    text-align: center;
    line-height: 1.5;
  }
  .rule-row {
    display: flex; align-items: center; gap: 16px;
  }
  .rule-row::before, .rule-row::after {
    content: ""; flex: 1; height: 1px;
  }
  .rule-row--right::after { background: var(--brand-gold); opacity: 0.85; }
  .rule-row--left::before { background: var(--brand-gold); opacity: 0.85; }
  .contact__name {
    color: var(--brand-gold);
    font-weight: 700;
    font-size: 23px;
    letter-spacing: 0.3px;
  }
  .contact__title {
    font-size: 17px;
    margin-bottom: 10px;
  }
  .contact__line { font-size: 17px; }
  .contact__label { color: var(--brand-gold); }
  .contact__company {
    color: var(--brand-gold);
    font-size: 18px;
    margin-top: 14px;
    letter-spacing: 0.3px;
  }
  .contact__address { font-size: 17px; }
</style>
</head>
<body>
  <main class="sheet">
    <section class="card card--front" aria-label="Card front">
      <div class="web-address">www.nwtelemetry.ca</div>
      <div class="lockup">
        <div class="wordmark">
          <span class="wordmark__square"></span>
          <span class="wordmark__name">Northwind</span>
        </div>
        <div class="established">EST 2001</div>
      </div>
    </section>

    <section class="card card--back" aria-label="Card back">
      <div class="back-logo">
        <div class="lockup">
          <div class="wordmark">
            <span class="wordmark__square"></span>
            <span class="wordmark__name">Northwind</span>
          </div>
          <div class="established">EST 2001</div>
        </div>
      </div>
      <div class="contact">
        <div class="rule-row rule-row--right">
          <span class="contact__name">DANIEL HARTWELL</span>
        </div>
        <div class="rule-row rule-row--left">
          <span class="contact__title">President and Chief Technical Officer</span>
        </div>
        <div class="contact__line">
          <span class="contact__label">T.</span> (555) 014-2290 |
          <span class="contact__label">E.</span> daniel@nwtelemetry.ca
        </div>
        <div class="contact__company">NORTHWIND TELEMETRY CORP.</div>
        <div class="contact__address">4410 – 8th Avenue SE, Unit 6, Calgary, Alberta T2X 1K4</div>
      </div>
    </section>
  </main>
</body>
</html>
```